Eye Catching Stylish Seminar Flyer

Design a Business Seminar Flyer that will be used for Print and Web distribution that is professional, eye catching in its color scheme and fonts.

have www.brightledgerday.com to register

Target Market(s)

Who is this for: business owners, marketplace professionals, homemakers.

Industry/Entity Type

Business Consultant

Font styles to use
Serif

Colors
abd037

Requirements
Must have
• Great colors, great Font
Nice to have
• Design a simple professional text based Logo for the Event that encapsulates For the flyer. Eye catching designs that provoke action in the reader of the flyer.
Should not have
• Cross designs stereotypical designs that are associated with religion. Rather they should be creative toward people that own businesses and work with colleagues in a daily office, school etc.

```html
<!DOCTYPE html>
<html lang="en">
<head>
<meta charset="utf-8">
<title>Seminar Flyer</title>
<link rel="stylesheet" href="https://fonts.googleapis.com/css2?family=Cinzel:wght@400;700&display=swap">
<style>
  :root{
    --backdrop:#a9a9ab;
    --paper:#f4f4f4;
    --maroon:#8b2f42;
    --wine:#9c3038;
    --orange:#c8573a;
    --clay:#b87060;
    --ink:#2b2424;
    --white:#ffffff;
  }
  *{margin:0;padding:0;box-sizing:border-box}
  html,body{width:1200px;height:911px;overflow:hidden;background:var(--backdrop)}
  body{font-family:"Cinzel",Georgia,serif;color:var(--ink)}
  .flyer{position:absolute;left:296px;top:25px;width:608px;height:860px;background:var(--paper);overflow:hidden;box-shadow:0 6px 18px rgba(0,0,0,.35)}
  .flyer-shapes{position:absolute;inset:0}
  .title-card{position:absolute;left:26px;top:150px;width:250px;height:220px;border-radius:16px;
    background:linear-gradient(135deg,#a3343c,var(--maroon));display:flex;align-items:center;justify-content:center;
    color:var(--white);text-align:center;font-size:20px;line-height:1.2;padding:18px;box-shadow:0 4px 10px rgba(0,0,0,.25)}
  .pill{display:inline-block;color:var(--white);border-radius:7px;padding:3px 12px;font-weight:700;letter-spacing:.5px}
  .pill-orange{background:var(--orange)}
  .pill-maroon{background:var(--maroon)}
  .info-box{position:absolute;border:1px solid var(--clay);border-radius:12px}
  .info-box .pill{position:absolute;left:40px;top:-20px;font-size:22px}
  .dates{left:50px;top:470px;width:260px;height:100px;padding:34px 20px 0}
  .dates p{font-size:14px;line-height:1.45;color:#4a3a3a}
  .fee{left:50px;top:612px;width:290px;height:120px;padding:34px 18px 0}
  .fee li{list-style:none;display:flex;gap:10px;font-size:11.5px;line-height:1.3;color:#5a4444;margin-bottom:8px}
  .tick{flex:none;margin-top:2px}
  .featuring{position:absolute;left:345px;top:365px;width:240px}
  .featuring .pill{font-size:20px;margin-bottom:12px}
  .speaker{display:flex;gap:12px;margin-bottom:7px}
  .bullet{flex:none;width:8px;height:8px;background:var(--orange);margin-top:8px}
  .speaker-name{font-size:16px;font-weight:700;color:#2a2222;line-height:1.3}
  .speaker-role{font-size:9.5px;color:#4a3a3a;letter-spacing:.3px}
  .event-mark{position:absolute;left:385px;top:652px;display:flex;align-items:center;gap:10px}
  .event-mark-square{flex:none;width:30px;height:30px;background:var(--maroon);border-radius:4px}
  .event-mark-name{font-size:19px;color:var(--maroon);line-height:1.1}
  .website{position:absolute;left:250px;top:825px;width:340px;display:flex;align-items:center;gap:10px;color:var(--white);font-size:16px;letter-spacing:1px}
  .website .rule{flex:1;height:1px;background:rgba(255,255,255,.8)}
</style>
</head>
<body>
<main class="flyer">
  <svg class="flyer-shapes" viewBox="0 0 608 860" width="608" height="860">
    <defs>
      <linearGradient id="photoTone" x1="0" y1="0" x2="1" y2="1">
        <stop offset="0" stop-color="#e7e2dc"/>
        <stop offset=".5" stop-color="#b89780"/>
        <stop offset="1" stop-color="#6d5a52"/>
      </linearGradient>
      <linearGradient id="bottomTone" x1="0" y1="1" x2="1" y2="0">
        <stop offset="0" stop-color="#a8705f"/>
        <stop offset="1" stop-color="#c8573a"/>
      </linearGradient>
    </defs>
    <rect role="img" aria-label="Photo of a presenter leading a seminar for seated colleagues" x="0" y="0" width="608" height="420" fill="url(#photoTone)"/>
    <path d="M0,400 Q260,250 608,255 L608,300 Q260,300 0,445 Z" fill="var(--maroon)"/>
    <path d="M0,455 Q280,300 608,285 L608,300 Q270,310 0,470 Z" fill="var(--orange)"/>
    <path d="M0,470 Q270,310 608,300 L608,860 L0,860 Z" fill="var(--paper)"/>
    <path d="M0,760 Q380,810 608,690 L608,860 L0,860 Z" fill="var(--maroon)"/>
    <path d="M0,785 Q390,835 608,720 L608,860 L0,860 Z" fill="url(#bottomTone)"/>
  </svg>

  <h1 class="title-card">The Voice of The Lord in the Marketplace: Moving from Intimacy to Impact</h1>

  <section class="info-box dates">
    <span class="pill pill-orange">Dates</span>
    <p>March 24th 6pm–9:20pm</p>
    <p>March 25th 8:30am–2:20pm</p>
  </section>

  <section class="info-box fee">
    <span class="pill pill-maroon">Fee: $30</span>
    <ul>
      <li><svg class="tick" width="11" height="11" viewBox="0 0 11 11"><rect x=".5" y=".5" width="10" height="10" fill="none" stroke="#c8573a"/><path d="M2 5.5 L4.5 8 L9 2.5" fill="none" stroke="#c8573a" stroke-width="1.4"/></svg>Includes continental breakfast, lunch, and light</li>
      <li><svg class="tick" width="11" height="11" viewBox="0 0 11 11"><rect x=".5" y=".5" width="10" height="10" fill="none" stroke="#c8573a"/><path d="M2 5.5 L4.5 8 L9 2.5" fill="none" stroke="#c8573a" stroke-width="1.4"/></svg>Refreshments throughout the conference.</li>
    </ul>
  </section>

  <section class="featuring">
    <span class="pill pill-maroon">Featuring</span>
    <div class="speaker"><span class="bullet"></span><div><div class="speaker-name">Marcus Ellery</div><div class="speaker-role">Author/Podcaster</div></div></div>
    <div class="speaker"><span class="bullet"></span><div><div class="speaker-name">Lena Ellery</div><div class="speaker-role">Writer</div></div></div>
    <div class="speaker"><span class="bullet"></span><div><div class="speaker-name">Owen Park</div><div class="speaker-role">Business Leader/Trainer</div></div></div>
    <div class="speaker"><span class="bullet"></span><div><div class="speaker-name">Rosa Delgado</div><div class="speaker-role">Business Owner</div></div></div>
    <div class="speaker"><span class="bullet"></span><div><div class="speaker-name">Thomas Hale</div><div class="speaker-role">Business Owner</div></div></div>
  </section>

  <div class="event-mark">
    <span class="event-mark-square"></span>
    <span class="event-mark-name">Bright Ledger<br>Day</span>
  </div>

  <div class="website"><span class="rule"></span><span>www.brightledgerday.com</span><span class="rule"></span></div>
</main>
</body>
</html>
```